Reputable business cards for Diplom Kauffrau, Privat und Geschäftslich

The business cards should be reputable, valuable and elegant in order to be able to use them for business. The design should also include a sophistication that is conspicuous. This could be a picture, an ornament, a sublime print or a kind of logo of the initials of my name "MK". The font should be clear and legible.
Target Market(s)
Business contacts, friends and acquaintances
Contact Information for Business Card
Diplom-Kauffrau Marietta Kuhnle
Lindenhofweg 37 50391 Haldenbrück
Mobil +49 170 418 29 57
e-mail marietta.kuhnle@postfeld.de
Font styles to use
Colors
Designer to choose colors to be used in the design.
Requirements
Must have
- Clear and easy to read font My name in larger font than the other information Visual conspicuity / specificity
Nice to have
- Different colors
Should not have
- Ornate font, playful

```html
<!DOCTYPE html>
<html lang="de">
<head>
<meta charset="utf-8">
<title>Marietta Kuhnle – Visitenkarte</title>
<link rel="stylesheet" href="https://fonts.googleapis.com/css2?family=Cinzel:wght@600;700&family=Lato:wght@400&display=swap">
<style>
  :root {
    --backdrop: #e4e4e6;
    --navy: #0b1c48;
    --paper: #ffffff;
    --cream: #f6f1e3;
    --ink: #1a2646;
  }
  * { margin: 0; padding: 0; box-sizing: border-box; }
  html, body {
    width: 1200px; height: 900px; overflow: hidden;
    background: var(--backdrop);
  }
  .canvas { position: relative; width: 1200px; height: 900px; }

  .card {
    position: absolute;
    width: 540px; height: 310px;
    border-radius: 28px;
    overflow: hidden;
    box-shadow: 0 6px 18px rgba(0,0,0,.18);
  }
  .card--back { left: 90px; top: 110px; background: var(--navy); }
  .card--front { left: 570px; top: 470px; background: var(--paper); }

  .monogram {
    font-family: "Cinzel", serif;
    font-weight: 700;
    line-height: 1;
    letter-spacing: 4px;
  }
  .card--back .monogram {
    position: absolute; left: 0; right: 0; top: 50%;
    transform: translateY(-50%);
    text-align: center;
    color: var(--paper);
    font-size: 84px;
  }

  .watermark {
    position: absolute; right: 28px; top: 100px;
    color: var(--cream);
    font-size: 110px;
  }
  .card--front .brand-mark {
    position: absolute; left: 36px; top: 96px;
    color: var(--navy);
    font-size: 50px;
  }
  .identity {
    position: absolute; left: 160px; top: 40px;
    color: var(--navy);
    z-index: 1;
  }
  .identity__name {
    font-family: "Cinzel", serif;
    font-weight: 700;
    font-size: 30px;
    letter-spacing: 1px;
    line-height: 1.1;
  }
  .identity__title {
    font-family: "Lato", sans-serif;
    font-size: 14px;
    letter-spacing: 5px;
    margin-top: 4px;
    padding-left: 60px;
  }

  .contact {
    position: absolute; left: 36px; bottom: 30px;
    font-family: "Lato", sans-serif;
    font-size: 16px;
    color: var(--ink);
    list-style: none;
    z-index: 1;
  }
  .contact li { display: flex; align-items: center; gap: 8px; line-height: 1.55; }
  .contact svg { width: 14px; height: 14px; fill: var(--ink); }
  .contact .contact__address { margin-top: 8px; }
</style>
</head>
<body>
<main class="canvas">
  <section class="card card--back" aria-label="Kartenrückseite">
    <div class="monogram">MK</div>
  </section>

  <section class="card card--front" aria-label="Kartenvorderseite">
    <div class="monogram watermark" aria-hidden="true">MK</div>
    <div class="monogram brand-mark">MK</div>
    <div class="identity">
      <h1 class="identity__name">Marietta Kuhnle</h1>
      <p class="identity__title">DIPLOM-KAUFFRAU</p>
    </div>
    <ul class="contact">
      <li>
        <svg viewBox="0 0 16 16" aria-hidden="true"><path d="M2 6c0-2 2-3 6-3s6 1 6 3v1h-3V5.5C10 5 9 4.8 8 4.8S6 5 5 5.5V7H2z"/><rect x="3" y="8" width="10" height="6" rx="1"/></svg>
        +49 170 418 29 57
      </li>
      <li>
        <svg viewBox="0 0 16 16" aria-hidden="true"><path d="M1 3h14v10H1z M2 4v.5l6 4.5 6-4.5V4z" fill-rule="evenodd"/></svg>
        marietta.kuhnle@postfeld.de
      </li>
      <li class="contact__address">Lindenhofweg 37, 50391 Haldenbrück</li>
    </ul>
  </section>
</main>
</body>
</html>
```